900mm double sided Card Ponytail Insert for hair

I need print ready file designs for card packaging inserts for my line of ponytails, These are two sided colour and fold at each end or contain the hair, for structure and so the brand is on display. These will be marketed as luxury ponytails, so we want a simple, soft but luxurious design feel. All the details are below but it will be the logo, photos and simple messaging

Target Market(s)

18-30 females

Industry/Entity Type

Beauty

Font styles to use
Serif

Requirements
Must have
• - Velmora Logo on the back and top front fold.
'Luxury Synthetic Ponytails' Head line
'For effortlessly long and luxurious hair' tag line
'For tutorials, questions and inspiration head to our 'Style Nook' on velmorabeauty.com'
www.velmorabeauty.com
Tag us on socials! @velmorabeautyofficial (snapvale and Chatlyne logos)
3 step-by-step pictures (holding pictures please until i have some taken)
Nice to have
• (notes to designers) view our website to see our branding velmorabeauty.com - it would be good to use our brand colours and somekind of tropical leaves maybe? i'm thinking palm leaves?
- my brand font is Sweet Getaway - but this may only be good for the biggest headings

```html
<!DOCTYPE html>
<html lang="en">
<head>
<meta charset="utf-8">
<title>Velmora Ponytail Insert</title>
<link rel="stylesheet" href="https://fonts.googleapis.com/css2?family=Playfair+Display:ital,wght@0,400;0,700;1,400;1,700&family=Quicksand:wght@400;700&display=swap">
<style>
:root{
  --pink:#e8417f;
  --mint:#6cc1a9;
  --mint-soft:#cfe6df;
  --mint-line:#b9ddd2;
  --gold:#c69a45;
  --ink:#333333;
  --paper:#ffffff;
  --backdrop:#ececec;
  --fold:#9a9a9a;
}
*{margin:0;padding:0;box-sizing:border-box}
html,body{width:1200px;height:4608px;overflow:hidden}
body{background:var(--backdrop);position:relative;font-family:"Quicksand",sans-serif}
.insert{position:absolute;left:360px;top:88px;width:480px;height:4432px;background:var(--paper)}
.abs{position:absolute}
.centered{left:0;width:100%;text-align:center}
.corner{position:absolute;left:0;width:480px}
.flip{transform:rotate(180deg)}
.fold-url{font-family:"Playfair Display",serif;font-size:22px;color:var(--ink);letter-spacing:1px}
.wordmark{font-family:"Playfair Display",serif;font-style:italic;color:var(--gold);font-size:84px;font-weight:400}
.fold-line{position:absolute;left:0;width:480px;border-top:3px dashed var(--fold)}
.panel{position:absolute;left:24px;top:744px;width:432px;height:3208px;border:3px solid var(--mint-line)}
.rule{position:absolute;left:90px;width:300px;height:2px;background:var(--gold)}
.rule::after{content:"";position:absolute;left:50%;top:-6px;width:14px;height:14px;margin-left:-7px;border-radius:50%;border:2px solid var(--gold);background:var(--paper)}
.headline{font-family:"Playfair Display",serif;font-style:italic;font-weight:700;color:var(--gold);font-size:70px;line-height:92px}
.tagline{font-family:"Playfair Display",serif;font-style:italic;color:var(--gold);font-size:38px;line-height:58px}
.photo-holder{position:absolute;left:40px;top:1444px;width:400px;height:1256px;background:var(--mint-soft);display:flex;align-items:center;justify-content:center}
.photo-holder span{font-family:"Playfair Display",serif;font-style:italic;color:var(--paper);font-size:28px;letter-spacing:2px}
.learn{position:absolute;left:40px;top:2744px;width:400px;height:680px;background:var(--pink)}
.learn-title{font-weight:700;color:var(--paper);font-size:52px;top:40px}
.learn-pill{position:absolute;left:70px;top:124px;width:260px;height:60px;border-radius:30px;background:var(--paper);color:var(--pink);font-weight:700;font-size:32px;line-height:60px;text-align:center}
.learn-list{position:absolute;left:0;top:210px;width:400px;height:370px;background:var(--mint)}
.learn-item{position:absolute;color:var(--paper);font-size:50px;display:flex;align-items:center;gap:14px}
.learn-url{position:absolute;left:0;top:594px;width:400px;height:64px;line-height:64px;color:var(--paper);font-weight:700;font-size:27px;text-align:center}
.people{position:absolute;left:40px;top:3470px;width:210px;height:380px;background:linear-gradient(180deg,#f7c7da,#f3a9c6 60%,#bfe3d8);border-radius:12px}
.heart{position:absolute;left:246px;top:3500px;width:200px;height:190px}
.heart-text{position:absolute;left:246px;top:3552px;width:200px;text-align:center;font-family:"Playfair Display",serif;font-style:italic;font-weight:700;color:var(--ink);font-size:32px;line-height:40px}
.socials{position:absolute;left:40px;top:3870px;width:400px;display:flex;justify-content:space-around;align-items:center;color:var(--pink);font-weight:700;font-size:30px}
.socials .hash{font-size:46px}
.handle{position:absolute;left:40px;top:3926px;width:400px;height:56px;line-height:56px;background:var(--pink);color:var(--paper);font-weight:700;font-size:26px;text-align:center}
.back-url{font-family:"Playfair Display",serif;font-weight:700;font-size:20px;color:var(--ink)}
</style>
</head>
<body>
<div class="insert">

  <!-- top fold -->
  <svg class="corner" style="top:0;height:200px" viewBox="0 0 480 200">
    <polygon points="0,0 480,0 480,70 0,140" fill="var(--pink)"/>
    <line x1="0" y1="158" x2="480" y2="88" stroke="var(--gold)" stroke-width="3"/>
  </svg>
  <div class="abs centered flip fold-url" style="top:276px">www.velmorabeauty.com</div>
  <div class="abs centered flip wordmark" style="top:390px">Velmora</div>
  <div class="fold-line" style="top:672px"></div>

  <!-- front panel -->
  <div class="panel"></div>
  <div class="rule" style="top:812px"></div>
  <h1 class="abs centered headline" style="top:862px">Luxury<br>Synthetic<br>Ponytails</h1>
  <div class="rule" style="top:1172px"></div>
  <p class="abs centered tagline" style="top:1220px">For effortlessly long<br>and luxurious hair</p>
  <div class="rule" style="top:1372px"></div>

  <div class="photo-holder" role="img" aria-label="Three step-by-step photos of attaching the ponytail"><span>3 STEPS PHOTO</span></div>

  <section class="learn">
    <div class="abs centered learn-title">Head to our</div>
    <div class="learn-pill">Style Nook</div>
    <div class="learn-list">
      <div class="learn-item" style="left:24px;top:20px">For
        <svg width="56" height="56" viewBox="0 0 56 56" fill="none" stroke="#fff" stroke-width="3"><path d="M10 46 L14 34 L40 8 L48 16 L22 42 Z"/><line x1="34" y1="14" x2="42" y2="22"/></svg>
      </div>
      <div class="learn-item" style="left:24px;top:100px">
        <svg width="56" height="50" viewBox="0 0 56 50" fill="none" stroke="#fff" stroke-width="3"><rect x="4" y="6" width="48" height="32" rx="3"/><polygon points="23,14 35,22 23,30" fill="#fff"/><line x1="18" y1="46" x2="38" y2="46"/></svg>
        Tutorials</div>
      <div class="learn-item" style="left:24px;top:190px">Questions ?</div>
      <div class="learn-item" style="left:24px;top:280px">
        <svg width="56" height="60" viewBox="0 0 56 60" fill="none" stroke="#fff" stroke-width="3"><path d="M28 6 A18 18 0 0 1 38 39 L38 46 L18 46 L18 39 A18 18 0 0 1 28 6 Z"/><line x1="20" y1="53" x2="36" y2="53"/></svg>
        Inspiration</div>
    </div>
    <div class="learn-url">www.velmorabeauty.com</div>
  </section>

  <div class="people" role="img" aria-label="Illustration of two young women taking a selfie together"></div>
  <svg class="heart" viewBox="0 0 200 190">
    <path d="M100 180 C40 130 6 100 6 58 C6 26 30 6 56 6 C76 6 92 18 100 34 C108 18 124 6 144 6 C170 6 194 26 194 58 C194 100 160 130 100 180 Z" fill="var(--mint-soft)" stroke="var(--pink)" stroke-width="4"/>
  </svg>
  <div class="heart-text">Tag us on<br>socials!</div>
  <div class="socials"><span class="hash">#</span><span>Chatlyne</span><span>Snapvale</span></div>
  <div class="handle">@velmorabeautyofficial</div>

  <!-- back fold -->
  <div class="fold-line" style="top:3984px"></div>
  <div class="abs centered wordmark" style="top:4070px">Velmora</div>
  <div class="abs centered back-url" style="top:4214px">www.velmorabeauty.com</div>
  <svg class="corner" style="top:4272px;height:160px" viewBox="0 0 480 160">
    <line x1="0" y1="92" x2="480" y2="22" stroke="var(--gold)" stroke-width="3"/>
    <polygon points="0,110 480,40 480,160 0,160" fill="var(--pink)"/>
  </svg>
</div>
</body>
</html>
```